Zielgruppe
Strandhaus mit Restaurant (Beach feeling)
Zielgruppe: gehoben, edel, teuer
Aufgabenstellung
Auf stilsicherheit und das es stylisch und gleichzeitig edel aussieht.
Format:
Breite 44,5
Höher 71
Text:
Logo oben gut sichtbar
Herzlich Willkommen! (andere Schriftart)
MONTAG - FREITAG
SAMSTAG - SONNTAG
Unsere Küche verwöhnt dich bis 21:00 Uhr - täglich frisch & mit Liebe gekocht.
Wolkenhain ist mehr als ein Ort - es ist ein Gefühl. (andere Schriftart)
Lindenmoor, Kastner Weg 58-60, 2791 Seefelden am Ried
www.wolkenhain-beispiel.at/reservieren

```html
<!DOCTYPE html>
<html lang="de">
<head>
<meta charset="utf-8">
<title>Wolkenhain – Öffnungszeiten</title>
<link rel="stylesheet" href="https://fonts.googleapis.com/css2?family=Lexend:wght@300;400;500;600&family=Great+Vibes&family=Playfair+Display:ital,wght@1,400;1,700&display=swap">
<style>
  :root {
    --page-bg: #ece9e4;
    --card-white: #ffffff;
    --sky: #72bfd1;
    --sea: #63b7c8;
    --foam: #d9eef0;
    --sand-light: #f6e3d4;
    --sand-warm: #efcfb2;
    --shore-blue: #cfe3e6;
    --sand-deep: #d9b27f;
    --teal: #3b7e8c;
    --ink: #1f2a2d;
    --gull-white: #e9eef0;
    --gull-grey: #9aa6ab;
  }
  * { box-sizing: border-box; margin: 0; padding: 0; }
  html, body {
    width: 1143px; height: 1200px; overflow: hidden;
    background: var(--page-bg);
  }
  .poster {
    position: absolute; left: 208px; top: 20px;
    width: 727px; height: 1160px;
    background: var(--card-white);
    box-shadow: 0 6px 24px rgba(0,0,0,.12);
  }
  .poster__scene {
    position: absolute; inset: 26px;
    overflow: hidden;
    background: linear-gradient(180deg,
      var(--sky) 0%, var(--sky) 24%,
      var(--sea) 30%, var(--foam) 35%,
      var(--sand-light) 40%, var(--sand-warm) 58%,
      var(--shore-blue) 70%, #d6e6e8 82%,
      var(--sand-light) 90%, var(--sand-deep) 100%);
  }
  .poster__frame {
    position: absolute; inset: 37px;
    border: 1.5px solid rgba(255,255,255,.95);
  }
  .gull {
    position: absolute; border-radius: 50%;
    background: radial-gradient(ellipse at center, var(--gull-white) 0%, var(--gull-grey) 60%, rgba(154,166,171,0) 72%);
    opacity: .85;
  }
  .gull--left { left: 51px; top: 85px; width: 169px; height: 180px; }
  .gull--right { left: 536px; top: 72px; width: 184px; height: 135px; }

  .brand {
    position: absolute; left: 0; right: 0; top: 148px;
    display: flex; justify-content: center; align-items: center; gap: 12px;
    font-family: "Lexend", sans-serif; font-weight: 500;
    font-size: 50px; color: var(--card-white); letter-spacing: 1px;
  }
  .brand__dot { width: 14px; height: 14px; border-radius: 50%; background: var(--card-white); }

  .welcome {
    position: absolute; left: 0; right: 0; top: 286px;
    text-align: center;
    font-family: "Great Vibes", cursive; font-weight: 400;
    font-size: 62px; color: var(--card-white); line-height: 1;
  }

  .hours {
    position: absolute; left: 82px; top: 441px;
    width: 562px; height: 359px;
    border-radius: 26px;
    background: rgba(255,251,247,.72);
    box-shadow: 6px 8px 14px rgba(0,0,0,.12);
    text-align: center;
    font-family: "Lexend", sans-serif; color: var(--teal);
  }
  .hours__days {
    position: absolute; left: 0; right: 0;
    font-size: 41px; font-weight: 600; letter-spacing: .5px; line-height: 1;
  }
  .hours__time {
    position: absolute; left: 0; right: 0;
    font-size: 27px; font-weight: 300; line-height: 1;
  }
  .hours__days--week { top: 37px; }
  .hours__time--week { top: 90px; }
  .hours__days--weekend { top: 147px; }
  .hours__time--weekend { top: 196px; }
  .hours__rule {
    position: absolute; left: 219px; top: 247px;
    width: 124px; height: 2px; background: var(--teal);
  }
  .hours__kitchen {
    position: absolute; left: 0; right: 0; top: 276px;
    font-size: 14px; font-weight: 300; color: var(--ink);
  }
  .hours__fresh {
    position: absolute; left: 0; right: 0; top: 298px;
    font-size: 21px; font-weight: 400; color: var(--ink);
  }

  .slogan {
    position: absolute; left: 0; right: 0; top: 860px;
    text-align: center; color: var(--teal);
    font-family: "Playfair Display", serif; font-style: italic;
  }
  .slogan__lead { display: block; font-size: 34px; font-weight: 400; line-height: 1.1; }
  .slogan__close { display: block; font-size: 42px; font-weight: 700; line-height: 1.1; margin-top: 2px; }

  .contact {
    position: absolute; left: 0; right: 0; top: 982px;
    text-align: center; font-style: normal;
    font-family: "Lexend", sans-serif; font-size: 16px; font-weight: 400;
    color: var(--ink); line-height: 24px;
  }
</style>
</head>
<body>
  <main class="poster">
    <div class="poster__scene" role="img" aria-label="Strandszene mit blauem Himmel, Meer, Wellen und hellem Sand"></div>
    <div class="poster__frame"></div>

    <div class="gull gull--left" role="img" aria-label="Fliegende Möwe"></div>
    <div class="gull gull--right" role="img" aria-label="Fliegende Möwe"></div>

    <div class="brand"><span class="brand__dot"></span>Wolkenhain</div>

    <h1 class="welcome">Herzlich Willkommen!</h1>

    <section class="hours">
      <div class="hours__days hours__days--week">MONTAG - FREITAG</div>
      <div class="hours__time hours__time--week">11:00 - 00:00</div>
      <div class="hours__days hours__days--weekend">SAMSTAG - SONNTAG</div>
      <div class="hours__time hours__time--weekend">09:00 - 00:00</div>
      <div class="hours__rule"></div>
      <p class="hours__kitchen">Unsere Küche verwöhnt dich bis 21:00 Uhr -</p>
      <p class="hours__fresh">täglich frisch &amp; mit Liebe gekocht.</p>
    </section>

    <p class="slogan">
      <span class="slogan__lead">Wolkenhain ist mehr als ein Ort -</span>
      <span class="slogan__close">es ist ein Gefühl.</span>
    </p>

    <address class="contact">
      Lindenmoor, Kastner Weg 58-60, 2791 Seefelden am Ried<br>
      www.wolkenhain-beispiel.at/reservieren
    </address>
  </main>
</body>
</html>
```